Web Design for Webdesign company 3 page PSD

Project
---------
We need a PSD Web Design to be used in a WordPress installation.
What we would like to create is a professional looking website for a web design agency. We also need you to look for suitable stock images to be placed on these pages.
We need the design for:
Homepage
Landing page
Contact page
attached in the pages file you will find a file with more in depth details how these files should be build up.
We would like to see a desktop version and a mobile version of these pages
The website should have a 1100px width.
The mobile design should have 480px width.
The homepage should have a header slider about 450px high.
The slider is preferred full width and should have some images text and a button
Objectives
-------------
The main objective for the website is to get leads from customers in the form of a request for a quotation or a call or mail me back action. The most important action for the homepage is to link and navigate to our landing pages.
What we want to tell our visitors (our main products)
-------------------------------------------------------------------
- A website with no big investment but a monthly rate
- A successful website with no worries (a complete website, seo, hosting and a service contract for future customization is included for a monthly rate)
Color Scheme
------------
Use branding colors. You can find them in the branding.pdf file.
Additional colors:
White: #ffffff
Black: #181818
Company info
--------------
We are a starting web design / marketing agency based in The Netherlands and looking for the design of our website. Our services are (custom) webdesign, website marketing or combinations of both. Our main customer group is small business owners.
We sell websites but give the option to buy it with a lease contract.
A second product is a default website with a complete service: SEO, hosting and a service contract for a monthly rate.
Content:
-----------
If not available place Lorem Ipsum text.
There will come about 400 words of text on the landing pages
Design Competition
--------------------------
Since this is a designing competition we would like to see your creativity.
What you can expect from us is a lot of feedback 7 days a week with short response time.
You can send us the first sketchy mock ups of the homepage and we will give feedback based on these design. But we like your feedback or comments as well
Read the pages file for more in depth details how the pages should be designed

Target Market(s)
Small business owners in The Netherlands
Industry/Entity Type
It Company
Number of Pages Required
3 page
Requirements
Must have
- Homepage:
- Header slider with images, some text and a link to a custom page
- The slider should have 3 designed slides
- Landings page:
- Sidebar
- Action button for a request for a quotation
- Action button for a call me back action
- Action button for an appointment
- Contact form:
- Address details
- Contact form
Nice to have
- Homepage:
- Full width slider
- Testimonial block
- Blog items
Should not have
- Flash
- A to crowded design

```html
<!DOCTYPE html>
<html lang="en">
<head>
<meta charset="utf-8">
<title>Birchline Web Studio</title>
<link href="https://fonts.googleapis.com/css2?family=Arimo:wght@400;700&family=Signika:wght@400;600&display=swap" rel="stylesheet">
<style>
  :root {
    --green: #5e9477;
    --green-dark: #3f7a5a;
    --mint: #c6f0d9;
    --teal: #347a86;
    --teal-head: #2f7a85;
    --sky: #6fc6da;
    --ink: #282627;
    --bar: #5f5f5f;
    --white: #ffffff;
    --light-text: #e4e4e4;
  }
  * { margin: 0; padding: 0; box-sizing: border-box; }
  html, body { width: 1148px; height: 1200px; overflow: hidden; background: var(--white); }
  body { font-family: "Arimo", Arial, sans-serif; }
  .page {
    position: relative; width: 1100px; height: 1150px;
    transform: scale(1.0436); transform-origin: 0 0;
  }
  .abs { position: absolute; }

  /* Header */
  .brand-name {
    left: 20px; top: 58px; font-family: "Arimo", Arial, sans-serif; font-weight: 700;
    font-size: 24px; line-height: 1; color: var(--teal-head);
  }
  .main-nav { left: 390px; top: 88px; display: flex; gap: 3px; }
  .main-nav a {
    display: block; width: 139px; height: 28px; background: var(--green);
    color: var(--white); text-decoration: none; text-align: center;
    font-size: 17px; line-height: 28px; letter-spacing: .3px;
  }
  .header-rule { left: 0; top: 119px; width: 1100px; height: 4px; background: var(--green); }

  /* Hero slider */
  .hero-title { left: 37px; top: 260px; font-family: "Signika", sans-serif; font-weight: 600; font-size: 47px; color: var(--teal-head); }
  .hero-sub { left: 110px; top: 333px; font-family: "Signika", sans-serif; font-size: 24px; color: var(--teal-head); }
  .hero-visual {
    left: 545px; top: 213px; width: 500px; height: 287px; border-radius: 6px;
    background: linear-gradient(160deg, #3a3a3a 0%, #9fc3dc 40%, #c6dbe9 65%, #4a4a4a 100%);
  }
  .slider-dots { left: 762px; top: 545px; display: flex; gap: 19px; }
  .slider-dots span { width: 18px; height: 18px; border-radius: 50%; background: var(--teal); }
  .slider-dots span.active { background: var(--sky); border: 2px solid var(--teal); }

  /* Feature band */
  .band-rule { left: 0; top: 575px; width: 1100px; height: 4px; background: var(--mint); }
  .band { left: 0; top: 579px; width: 1100px; height: 301px; background: var(--teal); }
  .card {
    top: 520px; width: 166px; height: 203px; border: 4px solid var(--mint);
    border-radius: 16px; background: var(--green); text-align: center;
    box-shadow: 0 2px 4px rgba(0,0,0,.25);
  }
  .card-photo { margin: 7px auto 0; width: 133px; height: 87px; background: linear-gradient(180deg, #8ea9b8, #5b6c63); }
  .card-photo.b { background: linear-gradient(180deg, #b9c2c9, #6f7a5d); }
  .card-photo.c { background: linear-gradient(180deg, #c79a3a, #3f5f74); }
  .card-title { margin-top: 12px; font-size: 13px; line-height: 15px; color: var(--light-text); }
  .card-btn {
    display: inline-block; margin-top: 20px; padding: 0 8px; height: 26px; line-height: 26px;
    background: var(--green-dark); color: var(--white); font-weight: 700; font-size: 13px;
    text-decoration: none; box-shadow: 0 2px 3px rgba(0,0,0,.3);
  }
  .intro-title { left: 543px; top: 612px; font-family: "Signika", sans-serif; font-weight: 600; font-size: 32px; font-variant: small-caps; color: var(--white); }
  .intro-text {
    left: 565px; top: 660px; width: 500px; font-weight: 700; font-size: 16px; line-height: 22.6px;
    font-variant: small-caps; color: var(--white); text-indent: 36px; letter-spacing: .5px;
  }

  /* Footer */
  .footer { left: 0; top: 880px; width: 1100px; height: 238px; background: var(--ink); }
  .footer-head { top: 921px; font-weight: 700; font-size: 17px; font-variant: small-caps; color: var(--sky); letter-spacing: .5px; }
  .footer-text { font-size: 12.5px; line-height: 15px; color: var(--white); }
  .post-list { left: 420px; top: 952px; list-style: none; }
  .post-list li { position: relative; padding-left: 15px; height: 30px; font-size: 13px; color: var(--white); }
  .post-list li::before { content: ""; position: absolute; left: 1px; top: 5px; width: 6px; height: 6px; border-radius: 50%; background: var(--teal); }
  .contact-icon { left: 818px; }
  .contact-line { left: 851px; font-size: 13px; color: var(--white); }
  .contact-line b { font-weight: 700; }

  .bottom-bar { left: 0; top: 1118px; width: 1100px; height: 32px; background: var(--bar); }
  .copyright { left: 45px; top: 1124px; font-size: 13px; font-weight: 700; color: #d0d0d0; }
  .bottom-nav { right: 19px; top: 1125px; font-size: 13px; font-weight: 700; color: #d8d8d8; }
  .bottom-nav a { color: #d8d8d8; text-decoration: none; }
  .bottom-nav span { margin: 0 4px; }
</style>
</head>
<body>
<div class="page">
  <header>
    <div class="abs brand-name">Birchline Web Studio</div>
    <nav class="abs main-nav">
      <a href="#">HOME</a><a href="#">PRODUCTS</a><a href="#">ABOUT US</a><a href="#">TESTIMONIALS</a><a href="#">INQUIRE</a>
    </nav>
    <div class="abs header-rule"></div>
  </header>

  <section>
    <h1 class="abs hero-title">Responsive Web Design</h1>
    <p class="abs hero-sub">Your website readable on all devices</p>
    <div class="abs hero-visual" role="img" aria-label="Desktop, tablet and phone screens showing a responsive testimonials page"></div>
    <div class="abs slider-dots"><span class="active"></span><span></span><span></span></div>
  </section>

  <section>
    <div class="abs band-rule"></div>
    <div class="abs band"></div>
    <article class="abs card" style="left:5px">
      <div class="card-photo" role="img" aria-label="Hotel pool terrace under trees"></div>
      <p class="card-title">INTEGER TINCIDUNT.<br>CRAS DAPIBUS.</p>
      <a class="card-btn" href="#">READ MORE</a>
    </article>
    <article class="abs card" style="left:176px">
      <div class="card-photo b" role="img" aria-label="Apartment building with garden"></div>
      <p class="card-title">VIVAMUS ELEMENTUM<br>SEMPER NISI.</p>
      <a class="card-btn" href="#">READ MORE</a>
    </article>
    <article class="abs card" style="left:347px">
      <div class="card-photo c" role="img" aria-label="Modern bar interior with stools"></div>
      <p class="card-title">AENEAN VULPUTATE<br>ELEIFEND TELLUS</p>
      <a class="card-btn" href="#">READ MORE</a>
    </article>
    <h2 class="abs intro-title">Lorem ipsum dolor sit amet</h2>
    <p class="abs intro-text">Aenean massa. Cum sociis natoque penatibus et magnis dis parturient montes, nascetur ridiculus mus. Donec quam felis, ultricies nec, pellentesque eu, pretium quis, sem. Nulla consequat massa quis enim. Donec pede justo, fringilla vel, aliquet nec, vulputate eget, arcu. In enim justo, rhoncus ut, imperdiet a, venenatis vitae, justo. Nullam dictum felis eu pede mollis pretium</p>
  </section>

  <footer>
    <div class="abs footer"></div>
    <h3 class="abs footer-head" style="left:32px">About The Company</h3>
    <p class="abs footer-text" style="left:47px;top:952px;width:262px">Aenean leo ligula, porttitor eu, consequat vitae, eleifend ac, enim. Aliquam lorem ante, dapibus in, viverra quis, feugiat a, tellus. Phasellus viverra nulla ut met varius laoreet.</p>
    <p class="abs footer-text" style="left:185px;top:1027px">-Donec Pede Justo</p>

    <h3 class="abs footer-head" style="left:412px">Recent Posts</h3>
    <ul class="abs post-list">
      <li>Aenean leo ligula, porttitor eu, consequat</li>
      <li>Vitae, eleifend ac, enim. Aliquam lorem ante,</li>
      <li>Dapibus in, viverra quis, feugiat a, tellus.</li>
      <li>Phasellus viverra nulla ut met varius laoreet.</li>
    </ul>

    <h3 class="abs footer-head" style="left:800px">Contact Information</h3>
    <svg class="abs contact-icon" style="top:949px" width="20" height="17" viewBox="0 0 20 17"><path d="M10 1 L1 9 H4 V16 H8 V11 H12 V16 H16 V9 H19 Z" fill="#347a86"/></svg>
    <p class="abs contact-line" style="top:950px"><b>52687</b> Vitae, eleifend ac,</p>
    <p class="abs contact-line" style="top:980px">Enim. Aliquam</p>
    <svg class="abs contact-icon" style="left:822px;top:1009px" width="13" height="21" viewBox="0 0 13 21"><rect x="1" y="1" width="11" height="19" rx="2" fill="none" stroke="#347a86" stroke-width="2"/><circle cx="6.5" cy="16.5" r="1.2" fill="#347a86"/></svg>
    <p class="abs contact-line" style="left:853px;top:1013px"><b>000-000-0000</b></p>
    <svg class="abs contact-icon" style="left:819px;top:1050px" width="21" height="14" viewBox="0 0 21 14"><rect width="21" height="14" fill="#347a86"/><path d="M0 0 L10.5 8 L21 0" fill="none" stroke="#282627" stroke-width="1.5"/></svg>
    <p class="abs contact-line" style="left:853px;top:1051px;font-size:11px;font-weight:700;font-variant:small-caps">hello@birchline.example</p>

    <div class="abs bottom-bar"></div>
    <p class="abs copyright">Copyright © 2015 Birchline Web Studio</p>
    <nav class="abs bottom-nav"><a href="#">HOME</a><span>|</span><a href="#">PRODUCTS</a><span>|</span><a href="#">ABOUT US</a><span>|</span><a href="#">TESTIMONIALS</a><span>|</span><a href="#">INQUIRE</a></nav>
  </footer>
</div>
</body>
</html>
```